Stationary for security company
BRAMLOCK GUARDING LTD
Project: Stationary for security company
Stationary for security company  - Security
Creative Brief
Professional
148 MORTWELL CRESCENT DUNSBY KENT TN8 4QP
info@bramlock-guarding.co.uk
I DON'T NEED ADDRESS ON BUSINESS CARDS, JUST ON THE LETTER HEADS PLEASE.
specialize in:- -CCTV SYSTEMS -INTRUDER ALARMS -INTERCOM SYSTEMS -ELECTRICAL INSTALLATIONS UNDERTAKEN
delwynparfitt delwynparfitt
#183 I was referring to the back design back option 3 but in blue and with out the text just logo in centre. Also could you do me a design for invoices too?
#183 Hello, thank you for your designs I like the idea you have in design #183. Could you remove the phone number from the logo itself and complete the bottom line. We don't really need a number on the logo as we will have it on the stationary itself! And also the back of the business card you have in the design in black could you do that in blue, I like the blue and remove the text writing from the back of the card, so we just have the logo on the back. One more thing could you add Facebook and Twitter to the front of the business card please. Kind regards Delwyn Parfitt

```html
<!DOCTYPE html>
<html lang="en">
<head>
<meta charset="utf-8">
<title>Bramlock Guarding Ltd – Business Card</title>
<link href="https://fonts.googleapis.com/css2?family=Open+Sans:wght@400;600;700;800&display=swap" rel="stylesheet">
<style>
  :root {
    --backdrop: #e6e6e8;
    --charcoal-top: #4a4a4d;
    --charcoal-bottom: #2c2c2e;
    --brand-blue: #1f49c4;
    --brand-blue-deep: #15359a;
    --paper: #ffffff;
    --text-light: #ffffff;
    --text-muted: #c9c9cc;
  }
  * { box-sizing: border-box; margin: 0; padding: 0; }
  html, body {
    width: 1200px;
    height: 906px;
    overflow: hidden;
    background: var(--backdrop);
    font-family: "Open Sans", Arial, sans-serif;
  }
  .canvas {
    position: relative;
    width: 1200px;
    height: 906px;
  }
  .card {
    position: absolute;
    top: 298px;
    width: 540px;
    height: 310px;
    overflow: hidden;
    box-shadow: 0 10px 28px rgba(0,0,0,0.18);
  }

  /* Contact side: rounded end on the right */
  .card--contact {
    left: 40px;
    border-radius: 16px 155px 155px 16px / 16px 155px 155px 16px;
    background: linear-gradient(180deg, var(--charcoal-top), var(--charcoal-bottom));
  }
  .card--contact .blue-band {
    position: absolute;
    left: 0; right: 0; bottom: 0;
    height: 112px;
    background: linear-gradient(180deg, var(--brand-blue), var(--brand-blue-deep));
  }
  .holder {
    position: absolute;
    left: 28px;
    top: 80px;
    color: var(--text-light);
  }
  .holder__name {
    font-weight: 800;
    font-size: 15px;
    letter-spacing: 0.3px;
  }
  .holder__title {
    font-size: 12px;
    color: var(--text-muted);
    margin-top: 3px;
  }
  .contact-list {
    position: absolute;
    left: 262px;
    top: 94px;
    list-style: none;
    font-size: 11.5px;
    color: var(--text-light);
    line-height: 1.6;
  }
  .contact-list b {
    font-weight: 700;
    display: inline-block;
    width: 66px;
  }

  /* Brand side: rounded end on the left */
  .card--brand {
    left: 620px;
    border-radius: 155px 16px 16px 155px / 155px 16px 16px 155px;
    background: var(--paper);
  }
  .card--brand .blue-band {
    position: absolute;
    left: 0; right: 0; bottom: 0;
    height: 138px;
    background: linear-gradient(180deg, var(--brand-blue), var(--brand-blue-deep));
  }
  .brand-mark {
    position: absolute;
    left: 40px; right: 0;
    top: 0;
    height: 172px;
    display: flex;
    align-items: center;
    justify-content: center;
    gap: 10px;
  }
  .brand-mark__dot {
    width: 14px;
    height: 14px;
    border-radius: 50%;
    background: var(--brand-blue);
  }
  .brand-mark__name {
    font-weight: 800;
    font-size: 22px;
    color: var(--brand-blue);
    letter-spacing: 0.2px;
  }
</style>
</head>
<body>
  <main class="canvas">
    <section class="card card--contact" aria-label="Business card contact side">
      <div class="blue-band"></div>
      <div class="holder">
        <p class="holder__name">MARCUS HOLLOWAY</p>
        <p class="holder__title">Principle, Creative Director</p>
      </div>
      <ul class="contact-list">
        <li><b>phone :</b>020 7946 0318</li>
        <li><b>email :</b>marcus@bramlock-guarding.co.uk</li>
        <li><b>twitter :</b>twitter.com/bramlockltd</li>
        <li><b>facebook :</b>facebook.com/bramlockguarding</li>
      </ul>
    </section>

    <section class="card card--brand" aria-label="Business card brand side">
      <div class="blue-band"></div>
      <div class="brand-mark">
        <span class="brand-mark__dot"></span>
        <span class="brand-mark__name">BRAMLOCK GUARDING LTD</span>
      </div>
    </section>
  </main>
</body>
</html>
```